Upcoming lecture sponsored by a church on an important topic

We have a Reformation The Speech coming up at the end of October on the topic of law and gospel. I thought it might be cool to use a flyer that looks like it was from that day and age. Picture what Conrad Velmer would advertise things on kind of an old church/reformation type format. It will be sponsored by our church, and we have a paragraph or two to describe the lecture that would be included on the flyer. We would also want it formatted so that it could be printed on postcards and mailed to churches and individuals.

The flyer should have the following paragraph...

The distinction between the law and the gospel is the most important distinction in the Christian faith. Conrad Velmer: “Distinguishing between the law and the gospel is the highest art in Christendom, one who every person who values the name Christian ought to recognize, know, and possess.” The distinction between the law and the gospel is of great comfort for the child of God. “For the law was given by Moses, but grace and truth came by Jesus Christ” (John 1:17). For these reasons, the distinction between the law and the gospel is the most heavily assaulted doctrine in the Christian faith. This Reformation Day, join us for an explanation and defense of the great distinction between God’s good law and God’s glorious gospel.

And the flyer should have the following information...

Topic: The Steady Word and the Bright Promise
Date and Time: Tuesday, October 31, 2023 at 7:30pm
Host: Harrow Creek Fellowship Church
Speaker: Rev. Gerald Voskuil
Venue: The Marlow Hall, 5172 Brenton Avenue, Hudsonville, MI 49318
Format: Lecture followed by Q&A and refreshments

00AB8E
00BBA5
67D7C9
C6EFE9
E9F9F6

• The color scheme that I would like to have is a teal color (the same color as found at www.brackenhollowchapel.com

```html
<!DOCTYPE html>
<html lang="en">
<head>
<meta charset="utf-8">
<title>Reformation Day Lecture – Flyer and Postcard</title>
<link rel="stylesheet" href="https://fonts.googleapis.com/css2?family=Cinzel:wght@400;600;700&family=Poppins:wght@300;400;500&display=swap">
<style>
  :root {
    --stage: #a9b1ba;
    --paper: #ebebeb;
    --white: #ffffff;
    --teal: #3c9aa3;
    --teal-deep: #1f5566;
    --ink: #111111;
    --body-ink: #1f5a6a;
  }
  * { margin: 0; padding: 0; box-sizing: border-box; }
  html, body { width: 1200px; height: 2803px; overflow: hidden; }
  body { background: var(--stage); position: relative; font-family: "Poppins", sans-serif; }

  .card { position: absolute; background: var(--paper); box-shadow: 2px 3px 4px rgba(0,0,0,.35); overflow: hidden; }
  .band-white { position: absolute; left: 0; right: 0; background: var(--white); }
  .frame-outer { position: absolute; border: 4px solid var(--teal); }
  .frame-inner { position: absolute; border: 1.5px solid var(--teal); }
  .rule { position: absolute; height: 4px; background: var(--teal); }
  .abs { position: absolute; left: 0; right: 0; text-align: center; }

  .series { font-family: "Cinzel", serif; font-weight: 700; color: var(--teal-deep); letter-spacing: 1px; }
  .topic { font-family: "Cinzel", serif; font-weight: 700; color: var(--teal); line-height: 1; letter-spacing: 1px; }
  .when { font-family: "Poppins", sans-serif; color: var(--teal); font-weight: 400; }
  .about { color: var(--body-ink); font-weight: 400; }
  .about p { text-align: justify; text-align-last: center; }
  .about p.lead { text-align: center; }

  .label { display: block; background: var(--teal); color: var(--white); font-family: "Cinzel", serif; font-weight: 400; text-align: center; letter-spacing: 1px; margin: 0 auto; }
  .detail { color: var(--ink); font-weight: 500; text-align: center; }

  /* Flyer */
  .flyer { left: 131px; top: 75px; width: 938px; height: 1326px; }
  .flyer .series { top: 90px; font-size: 45px; }
  .flyer .topic { top: 271px; font-size: 71px; }
  .flyer .topic span { display: block; height: 73px; }
  .flyer .when { top: 490px; font-size: 39px; line-height: 47px; }
  .flyer .about { left: 96px; right: 96px; top: 660px; font-size: 18.6px; line-height: 22.8px; }
  .flyer .about p { margin-bottom: 22.8px; }
  .flyer .facts { position: absolute; top: 1046px; left: 0; right: 0; }
  .flyer .fact { position: absolute; width: 300px; }
  .flyer .label { width: 168px; height: 28px; font-size: 21px; line-height: 28px; }
  .flyer .detail { font-size: 18.6px; line-height: 23px; margin-top: 5px; }
  .flyer .venue { position: absolute; left: 0; right: 0; top: 1207px; }
  .flyer .venue .detail { margin-top: 4px; }

  /* Postcard front */
  .post-front { left: 160px; top: 1479px; width: 882px; height: 587px; }
  .post-front .series { top: 60px; font-size: 32px; }
  .post-front .topic { top: 144px; font-size: 42px; }
  .post-front .topic span { display: block; height: 45px; }
  .post-front .when { top: 249px; font-size: 23.5px; }
  .post-front .about { left: 90px; right: 90px; top: 306px; font-size: 14.1px; line-height: 17.2px; }
  .post-front .about p { margin-bottom: 17px; }

  /* Postcard back */
  .post-back { left: 160px; top: 2106px; width: 882px; height: 587px; }
  .post-back .fact { position: absolute; left: 35px; width: 454px; }
  .post-back .label { width: 217px; height: 27px; font-size: 22px; line-height: 27px; }
  .post-back .detail { font-size: 20.5px; line-height: 24.5px; margin-top: 3px; }
  .stamp { position: absolute; left: 756px; top: 29px; width: 82px; height: 82px; background: var(--white); }
  .address-line { position: absolute; left: 516px; width: 322px; height: 0; border-top: 1.5px dotted #444; }
</style>
</head>
<body>

<!-- Flyer -->
<section class="card flyer">
  <div class="band-white" style="top:175px;height:459px;"></div>
  <div class="frame-outer" style="left:29px;top:32px;width:880px;height:1202px;border-bottom:none;"></div>
  <div class="rule" style="left:29px;top:1230px;width:266px;"></div>
  <div class="rule" style="left:608px;top:1230px;width:301px;"></div>
  <div class="frame-inner" style="left:45px;top:55px;width:847px;height:1157px;"></div>

  <h2 class="abs series">REFORMATION DAY LECTURE</h2>
  <div class="rule" style="left:146px;top:255px;width:646px;"></div>
  <h1 class="abs topic"><span>THE STEADY WORD &amp;</span><span>THE BRIGHT PROMISE</span></h1>
  <div class="rule" style="left:146px;top:426px;width:646px;"></div>
  <p class="abs when">OCTOBER 31, 2023<br>7:30PM</p>

  <div class="abs about">
    <p class="lead">The distinction between the law and the gospel is the<br>most important distinction in the Christian faith.</p>
    <p>Conrad Velmer: “Distinguishing between the law and the gospel is the highest art in Christendom, one who every person who values the name Christian ought to recognize, know, and possess.”</p>
    <p>The distinction between the law and the gospel is of great comfort for the child of God. “For the law was given by Moses, but grace and truth came by Jesus Christ” (John 1:17).</p>
    <p>For these reasons, the distinction between the law and the gospel is the most heavily assaulted doctrine in the Christian faith. This Reformation Day, join us for an explanation and defense of the great distinction between God’s good law and God’s glorious gospel.</p>
  </div>

  <div class="facts">
    <div class="fact" style="left:46px;">
      <span class="label">HOST</span>
      <p class="detail">Harrow Creek Fellowship<br>Church<br>www.brackenhollowchapel.com</p>
    </div>
    <div class="fact" style="left:336px;">
      <span class="label">SPEAKER</span>
      <p class="detail">Rev. Gerald Voskuil</p>
    </div>
    <div class="fact" style="left:626px;">
      <span class="label">FORMAT</span>
      <p class="detail">Lecture followed<br>by Q&amp;A<br>and refreshments</p>
    </div>
  </div>

  <div class="venue" style="left:-16px;">
    <span class="label" style="width:168px;height:28px;font-size:21px;line-height:28px;">VENUE</span>
    <p class="detail" style="font-size:18.6px;margin-left:16px;">The Marlow Hall, 5172 Brenton Avenue, Hudsonville, MI 49318</p>
  </div>
</section>

<!-- Postcard front -->
<section class="card post-front">
  <div class="band-white" style="top:111px;height:184px;"></div>
  <div class="frame-outer" style="left:35px;top:31px;width:812px;height:526px;"></div>
  <div class="frame-inner" style="left:52px;top:46px;width:778px;height:494px;"></div>

  <h2 class="abs series">REFORMATION DAY LECTURE</h2>
  <div class="rule" style="left:213px;top:133px;width:455px;height:3px;"></div>
  <h1 class="abs topic"><span>THE STEADY WORD &amp;</span><span>THE BRIGHT PROMISE</span></h1>
  <div class="rule" style="left:213px;top:237px;width:455px;height:3px;"></div>
  <p class="abs when">OCTOBER 31, 2023 AT 7:30PM</p>

  <div class="abs about">
    <p class="lead">The distinction between the law and the gospel is the<br>most important distinction in the Christian faith.</p>
    <p>Conrad Velmer: “Distinguishing between the law and the gospel is the highest art in Christendom, one who every person who values the name Christian ought to recognize, know, and possess.</p>
    <p>“ The distinction between the law and the gospel is of great comfort for the child of God. “For the law was given by Moses, but grace and truth came by Jesus Christ” (John 1:17).</p>
    <p>For these reasons, the distinction between the law and the gospel is the most heavily assaulted doctrine in the Christian faith. This Reformation Day, join us for an explanation and defense of the great distinction between God’s good law and God’s glorious gospel.</p>
  </div>
</section>

<!-- Postcard back -->
<section class="card post-back">
  <div class="frame-outer" style="left:35px;top:30px;width:454px;height:529px;"></div>
  <div class="frame-inner" style="left:50px;top:44px;width:424px;height:501px;"></div>

  <div class="fact" style="top:72px;">
    <span class="label">HOST</span>
    <p class="detail">Harrow Creek Fellowship Church<br>www.brackenhollowchapel.com</p>
  </div>
  <div class="fact" style="top:193px;">
    <span class="label">SPEAKER</span>
    <p class="detail">Rev. Gerald Voskuil</p>
  </div>
  <div class="fact" style="top:289px;">
    <span class="label">FORMAT</span>
    <p class="detail">Lecture followed by<br>Q&amp;A and refreshments</p>
  </div>
  <div class="fact" style="top:411px;">
    <span class="label">VENUE</span>
    <p class="detail">The Marlow Hall,<br>5172 Brenton Avenue, Hudsonville,<br>MI 49318</p>
  </div>

  <div class="stamp"></div>
  <div class="address-line" style="top:209px;"></div>
  <div class="address-line" style="top:291px;"></div>
  <div class="address-line" style="top:372px;"></div>
  <div class="address-line" style="top:453px;"></div>
</section>

</body>
</html>
```